Wine Label for a wine from Tuscany, Italy

We need a wine label for a white and red wine, can be the same label or can be somewhat differentiated with any variation you feel would be good.. These two wines come from Tuscany, Italy. Wine labels from Tuscany Italy tend to be traditional. We are open to traditional looking labels but also more modern, eye catching too. We want to convey a sense of elegance, importance, great wine. I am attaching some examples of labels we like from Tuscany, also a label that was designed for us recently by one of you, which we LOVE. No wine glasses, wine bottles or grapes featured on the label please. We tend to like the white background. No blue please.

Target Market(s)

More women than men purchase wine, but it needs to appeal to both sexes.

Requirements
Must have
• Wine Name: Corte L' or Corte l'
• Type/Varletal: Rosso Toscano (White is Vermentino)
• Vintage (year): 2018
• That is all the text we want on the label, thanks
Nice to have
• Clean, something that makes someone want to grab this wine bottle off the shelf!
Should not have
• Images of Wine glass, wine bottles, grapes
• Do not use the color blue please.

```html
<!DOCTYPE html>
<html lang="en">
<head>
<meta charset="utf-8">
<title>Corte L' Rosso Toscano 2018 – Label Range</title>
<link rel="stylesheet" href="https://fonts.googleapis.com/css2?family=Ubuntu:wght@500;700&display=swap">
<style>
  :root {
    --backdrop: #ececec;
    --label-paper: #fbfbfb;
    --emboss-fill: #f6f6f6;
    --emboss-shade: rgba(0, 0, 0, 0.16);
    --emboss-light: rgba(255, 255, 255, 0.95);
    --ink-rosso: #5c0b0b;
    --ink-rosato: #c8321a;
    --ink-bianco: #b7860f;
  }
  * { margin: 0; padding: 0; box-sizing: border-box; }
  html, body {
    width: 1200px;
    height: 1200px;
    overflow: hidden;
    background: var(--backdrop);
  }
  .label-range {
    position: relative;
    width: 1200px;
    height: 1200px;
    display: flex;
    justify-content: center;
    align-items: center;
    gap: 60px;
  }
  .wine-label {
    position: relative;
    width: 300px;
    height: 540px;
    background: var(--label-paper);
    box-shadow: 0 1px 3px rgba(0, 0, 0, 0.08);
  }
  .initial-emboss {
    position: absolute;
    left: 41px;
    top: 115px;
    width: 215px;
    height: 244px;
    overflow: visible;
  }
  .initial-emboss path {
    fill: var(--emboss-fill);
    filter: drop-shadow(-1px -1px 0 var(--emboss-light)) drop-shadow(2px 2px 2px var(--emboss-shade));
  }
  .label-text {
    position: absolute;
    left: 43px;
    top: 418px;
    font-family: "Ubuntu", sans-serif;
    font-weight: 700;
    line-height: 1;
  }
  .wine-name {
    font-size: 28px;
    font-weight: 500;
    margin-bottom: 8px;
  }
  .wine-type,
  .wine-vintage {
    font-size: 19px;
    margin-bottom: 6px;
  }
  .label--rosso .label-text { color: var(--ink-rosso); }
  .label--rosato .label-text { color: var(--ink-rosato); }
  .label--bianco .label-text { color: var(--ink-bianco); }
</style>
</head>
<body>
  <main class="label-range">
    <section class="wine-label label--rosso">
      <svg class="initial-emboss" viewBox="0 0 215 244" aria-hidden="true">
        <path d="M0 0 H100 V154 H215 V244 H0 Z"/>
      </svg>
      <div class="label-text">
        <p class="wine-name">Corte L</p>
        <p class="wine-type">Rosso Toscano</p>
        <p class="wine-vintage">2018</p>
      </div>
    </section>

    <section class="wine-label label--rosato">
      <svg class="initial-emboss" viewBox="0 0 215 244" aria-hidden="true">
        <path d="M0 0 H100 V154 H215 V244 H0 Z"/>
      </svg>
      <div class="label-text">
        <p class="wine-name">Corte L</p>
        <p class="wine-type">Rosso Toscano</p>
        <p class="wine-vintage">2018</p>
      </div>
    </section>

    <section class="wine-label label--bianco">
      <svg class="initial-emboss" viewBox="0 0 215 244" aria-hidden="true">
        <path d="M0 0 H100 V154 H215 V244 H0 Z"/>
      </svg>
      <div class="label-text">
        <p class="wine-name">Corte L</p>
        <p class="wine-type">Rosso Toscano</p>
        <p class="wine-vintage">2018</p>
      </div>
    </section>
  </main>
</body>
</html>
```